Torvane Template Design for Pressmoor Quillpath Site

We need graphic design and theme design work for our new site that will be running Quillpath with Torvane as the theme.

We have a draft logo that needs a graphic designer to improve it.

We are looking for sleek, modern, design that while minimal is distinct. ie page elements, content enhancement, block design that can be used, reused by in-house team.
This means there will also need to be a guide created on how to create, insert, edit each of those elements so that they can be used on new pages over time.

We have several businesses for which this is the "umbrella company" and so we will want to unify the colours and have identified a palette from which to start.

Some examples of site design we would like to stand up like:
https://www.zlt-example.com/
https://latchpromo-example.com/
https://business.veltrix-example.com/
https://www.norvask-example.com/learning/home.aspx

When I say "coded" below, this really just means the CSS needed for page elements.

Target Market(s)

Small firms in professional services - engineers, land surveyors, consultants

Number of Pages Required

3 page

Font styles to use
Sans Serif

Requirements
Must have
• Pressmoor/Torvane as base template, full home page layout with lorem ipsum placeholder
Nice to have
• custom blocks for pull quotes, call to action, a better design on the logo so it doesn't look like a rainbow.
Should not have
• Need for Blockwright

```html
<!DOCTYPE html>
<html lang="en">
<head>
<meta charset="utf-8">
<title>Veridan — Professional Development</title>
<link rel="stylesheet" href="https://fonts.googleapis.com/css2?family=Plus+Jakarta+Sans:ital,wght@0,400;0,500;0,600;0,700;0,800;1,400&display=swap">
<style>
:root{
  --ink:#0f1730;
  --text:#2a3350;
  --muted:#5b6480;
  --blue:#1d4ed8;
  --blue-bright:#2b5be8;
  --navy:#0a1f4d;
  --navy-deep:#061334;
  --footer:#141a33;
  --teal:#4a7c7c;
  --line:#e6e8ee;
  --soft:#f6f7fa;
  --slate:#8c9ab3;
  --white:#ffffff;
}
*{box-sizing:border-box;margin:0;padding:0}
html,body{width:1200px;height:3112px;overflow:hidden}
body{font-family:"Plus Jakarta Sans",Arial,sans-serif;color:var(--text);background:var(--white)}
.wrap{width:800px;margin:0 auto;position:relative}
.btn{display:inline-flex;align-items:center;justify-content:center;font-size:10.5px;font-weight:600;border-radius:4px;height:30px;padding:0 16px;text-decoration:none}
.btn-primary{background:var(--blue);color:var(--white)}
.btn-ghost{border:1px solid var(--line);color:var(--ink);background:var(--white)}

/* nav */
.site-nav{height:51px;border-bottom:1px solid var(--line);display:flex;align-items:center;padding:0 50px 0 60px}
.brand{font-size:16px;font-weight:600;color:var(--ink);letter-spacing:-.3px}
.nav-links{display:flex;gap:26px;margin-left:auto;margin-right:auto;padding-left:150px;font-size:9.5px;color:var(--text)}
.nav-actions{display:flex;gap:10px}
.nav-actions .btn{height:25px;font-size:9.5px;padding:0 19px}

/* hero */
.hero{height:432px;position:relative;text-align:center;color:var(--white);overflow:hidden}
.hero-photo{position:absolute;inset:0;background:linear-gradient(100deg,#1b2547 0%,#2c3a66 35%,#4a5474 60%,#6b6f82 100%)}
.hero-inner{position:relative;padding-top:74px}
.hero h1{font-size:48px;font-weight:800;letter-spacing:-1.5px;line-height:1.1}
.hero h1 span{color:var(--blue-bright)}
.hero .lead{font-size:14.5px;font-weight:600;line-height:1.25;width:400px;margin:12px auto 18px}
.hero .copy{font-size:10.5px;line-height:17.5px;width:420px;margin:0 auto;color:#e7eaf3}
.hero-ctas{display:flex;gap:10px;justify-content:center;margin-top:39px}
.hero-ctas .btn{height:37px;width:140px}
.btn-outline-light{border:1px solid rgba(255,255,255,.8);color:var(--white)}

/* pathways */
.pathways{height:405px;padding-top:48px}
.section-title{font-size:20px;font-weight:700;color:var(--ink);letter-spacing:-.5px}
.pathways .intro{font-size:10px;line-height:17.5px;margin:14px 0 0 2px;width:420px}
.pathways .intro strong{font-weight:700;color:var(--ink)}
.cards{display:flex;gap:16px;margin-top:14px}
.card{width:148px;height:138px;border:1px solid var(--line);border-radius:6px;padding:16px 15px}
.pill{display:inline-block;font-size:6.5px;font-weight:700;color:var(--blue);background:#e8eefc;border-radius:3px;padding:3px 5px}
.card h3{font-size:11.5px;font-weight:600;color:var(--ink);line-height:17px;margin:10px 0 8px}
.card p{font-size:8.5px;line-height:14px;color:var(--muted)}
.pathways .note{font-size:10px;line-height:15px;margin:22px 0 0 2px}

/* difference */
.difference{height:542px;position:relative;overflow:hidden}
.difference-bg{position:absolute;inset:0;background:radial-gradient(ellipse at 40% 55%,#123a86 0%,#0b2660 35%,var(--navy-deep) 80%)}
.difference .wrap{display:flex;justify-content:space-between;padding-top:74px}
.diff-left{width:395px;color:var(--white)}
.diff-left h2{font-size:31px;font-weight:800;line-height:32px;letter-spacing:-1px;margin-top:9px}
.diff-left p{font-size:12.5px;line-height:17.5px;margin-top:22px}
.diff-photo{width:370px;height:188px;margin-top:18px;border-radius:4px;background:linear-gradient(120deg,#3a2412 0%,#a5622a 45%,#d89a5a 60%,#5a3418 100%)}
.combine{width:370px;height:376px;background:var(--white);border-radius:8px;padding:32px 30px}
.combine h3{font-size:15px;font-weight:700;color:var(--ink)}
.combine ul{list-style:none;margin-top:20px}
.combine li{display:flex;gap:10px;font-size:11px;line-height:15px;color:var(--text);margin-bottom:17.5px}
.combine li svg{flex:none;width:13px;height:13px;margin-top:1px}
.combine blockquote{font-size:10px;font-style:italic;line-height:16px;color:var(--muted);margin-top:46px}

/* advisory */
.advisory{height:594px;padding-top:62px}
.advisory .sub{font-size:10px;margin-top:7px}
.advisory .label{font-size:10px;font-weight:700;color:var(--ink);margin-top:22px}
.services{margin-top:14px;border-top:1px solid var(--line)}
.service{height:86px;display:flex;align-items:center;padding:0 12px}
.service.alt{background:var(--soft)}
.service svg.icon{width:13px;height:13px;flex:none}
.service h3{width:216px;font-size:15px;font-weight:600;color:var(--ink);margin-left:16px}
.service p{width:340px;font-size:11px;line-height:17.5px;color:var(--text)}
.service .arrow{margin-left:auto;width:12px;height:12px}
.advisory .close{font-size:9.5px;text-align:center;margin-top:14px;color:var(--text)}

/* featured */
.featured{height:466px;background:var(--soft);padding-top:53px}
.featured-card{width:748px;height:370px;margin:0 auto;border-radius:14px;background:radial-gradient(ellipse at 50% 75%,#123f91 0%,#0a2a6b 45%,#081c49 100%);text-align:center;color:var(--white);padding-top:50px}
.badge{width:34px;height:34px;border-radius:50%;background:var(--white);display:flex;align-items:center;justify-content:center;margin:0 auto}
.featured-card h2{font-size:22px;font-weight:700;letter-spacing:-.6px;margin-top:18px}
.featured-card p{font-size:12.5px;line-height:17.5px;width:460px;margin:16px auto 0;color:#e2e7f4}
.featured-card .btn{height:43px;width:165px;font-size:11.5px;margin-top:30px}

/* closing cta */
.closing{height:355px;text-align:center;padding-top:78px}
.closing h2{font-size:40px;font-weight:800;line-height:38px;letter-spacing:-1.2px;color:var(--ink);width:540px;margin:0 auto}
.closing h2 span{color:var(--slate)}
.closing p{font-size:13px;line-height:17.5px;margin-top:31px;color:var(--ink)}
.closing-ctas{display:flex;gap:10px;justify-content:center;margin-top:26px}
.closing-ctas .btn{height:36px;font-size:10.5px;padding:0 15px}
.btn-teal{background:var(--teal);color:var(--white)}

/* footer */
.site-footer{height:267px;background:var(--footer);color:#aab1c7;padding-top:53px}
.footer-cols{display:flex}
.footer-cols > div{width:208px}
.footer-brand{font-size:16px;font-weight:700;color:var(--white);margin-top:2px}
.footer-cols .about{font-size:8.5px;line-height:14px;margin-top:14px;width:170px}
.footer-cols h4{font-size:10px;font-weight:600;color:var(--white)}
.footer-cols ul{list-style:none;margin-top:16px}
.footer-cols li{font-size:8.5px;margin-bottom:9px}
.subscribe p{font-size:8.5px;margin-top:16px}
.sub-form{display:flex;gap:6px;margin-top:13px}
.sub-input{width:137px;height:24px;border-radius:3px;background:#222a45;border:1px solid #2d3553;font-size:8.5px;padding:0 10px;display:flex;align-items:center;color:#6f789a}
.sub-btn{width:35px;height:24px;border-radius:3px;background:var(--blue);display:flex;align-items:center;justify-content:center}
.footer-bottom{display:flex;justify-content:space-between;border-top:1px solid #262e4a;margin-top:58px;padding-top:22px;font-size:7.5px;color:#6f789a}
.footer-bottom nav{display:flex;gap:15px}
</style>
</head>
<body>

<header class="site-nav">
  <div class="brand">Veridan</div>
  <nav class="nav-links"><span>Platform</span><span>Learning</span><span>Resources</span><span>Podcast</span><span>Coaching</span></nav>
  <div class="nav-actions"><a class="btn btn-ghost">Login</a><a class="btn btn-primary">Book a Conversation</a></div>
</header>

<section class="hero">
  <div class="hero-photo" role="img" aria-label="Angled glass facade of a modern office tower under a dusky sky"></div>
  <div class="hero-inner">
    <h1>Welcome to <span>Veridan</span></h1>
    <p class="lead">Professional development for firms that want more than just credits.</p>
    <p class="copy">Veridan is a continuing education and leadership platform built for professional service firms that want to strengthen profit, leadership, culture, and long-term value.<br>We are not simply a course provider.<br>We are a business advisory ecosystem — and this platform is where our frameworks, tools, and experience become accessible, structured, and scalable.</p>
    <div class="hero-ctas"><a class="btn btn-primary">Explore the Platform</a><a class="btn btn-outline-light">Book a Conversation</a></div>
  </div>
</section>

<section class="pathways">
  <div class="wrap">
    <h2 class="section-title">Learning That Builds Real Firms</h2>
    <p class="intro">Inside Veridan, you'll find structured learning paths and targeted modules designed to move you from reactive operator to intentional leader.<br><strong>Our core pathways include:</strong></p>
    <div class="cards">
      <article class="card"><span class="pill">6 HRS</span><h3>Leadership Foundations</h3><p>Vision, values, business development, leadership identity</p></article>
      <article class="card"><span class="pill">4 HRS</span><h3>Management Essentials</h3><p>Compensation, delegation, coaching, crucial conversations</p></article>
      <article class="card"><span class="pill">8 HRS</span><h3>Finance for Firm Owners</h3><p>Financial fluency, margin awareness, KPI tracking</p></article>
      <article class="card"><span class="pill">5 HRS</span><h3>Operational Excellence</h3><p>Systems, SOPs, automation foundations</p></article>
      <article class="card"><span class="pill">6 HRS</span><h3>The Profitable Firm Blueprint</h3><p>Client communication and sustainable performance</p></article>
    </div>
    <p class="note">Courses are practical, implementation-focused, and designed to support professionals operating within regulated environments. We align content with common Canadian CPD structures so learning hours can support professional development requirements.<br>You gain credits — and capability</p>
  </div>
</section>

<section class="difference">
  <div class="difference-bg"></div>
  <div class="wrap">
    <div class="diff-left">
      <h2>What Makes Veridan Different</h2>
      <p>Most CE platforms deliver information.<br>We deliver integration.<br>Our content connects leadership, finance, compensation, culture, and operations into one shared language. Owners and managers learn overlapping concepts so firms align — not fragment.</p>
      <div class="diff-photo" role="img" aria-label="Close-up of a stack of aged paper documents in warm light"></div>
    </div>
    <div class="combine">
      <h3>We combine:</h3>
      <ul>
        <li><svg viewBox="0 0 14 14" fill="none" stroke="#1d4ed8" stroke-width="1.3"><rect x="1.5" y="2.5" width="11" height="9" rx="1.5"/><path d="M5 5.5h5M5 8.5h3"/></svg>Financial rigor and margin literacy</li>
        <li><svg viewBox="0 0 14 14" fill="none" stroke="#1d4ed8" stroke-width="1.3"><path d="M7 1.5a5 5 0 0 0-3 9v2h4v-1.5a5 5 0 0 0-1-9.5z"/><circle cx="7" cy="6" r="1.5"/></svg>Leadership identity and culture design</li>
        <li><svg viewBox="0 0 14 14" fill="none" stroke="#1d4ed8" stroke-width="1.3"><rect x="1.5" y="3" width="11" height="7" rx="1"/><circle cx="7" cy="6.5" r="1.6"/><path d="M1.5 12h11"/></svg>Compensation tied to performance and profitability</li>
        <li><svg viewBox="0 0 14 14" fill="none" stroke="#1d4ed8" stroke-width="1.3"><circle cx="3.5" cy="3" r="1.5"/><circle cx="3.5" cy="11" r="1.5"/><circle cx="10.5" cy="7" r="1.5"/><path d="M3.5 4.5v5M3.5 7h5.5"/></svg>Delegation frameworks and accountability systems</li>
        <li><svg viewBox="0 0 14 14" fill="none" stroke="#1d4ed8" stroke-width="1.3"><path d="M1.5 11l4-4 2.5 2.5 4.5-5"/><path d="M9 4.5h3.5V8"/></svg>Business planning connected to KPIs and<br>measurable outcomes</li>
        <li><svg viewBox="0 0 14 14" fill="none" stroke="#1d4ed8" stroke-width="1.3"><path d="M1.5 3h6M4.5 1.5V3M3 3c.5 3 2 4.5 4 5.5M6.5 3c-.5 3-2.5 5-5 6M7.5 12.5l2.5-6 2.5 6M8.3 10.5h3.4"/></svg>A shared language of leadership and management</li>
      </ul>
      <blockquote>"This platform reflects real-world advice scaled to professional service firms."</blockquote>
    </div>
  </div>
</section>

<section class="advisory">
  <div class="wrap">
    <h2 class="section-title">Beyond Courses: A Complete Advisory Relationship</h2>
    <p class="sub">Veridan is the hub — but it's not the limit.</p>
    <p class="label">We also offer:</p>
    <div class="services">
      <div class="service">
        <svg class="icon" viewBox="0 0 14 14" fill="none" stroke="#1d4ed8" stroke-width="1.4"><path d="M2 5.5h2l4-3v9l-4-3H2z"/><path d="M10.5 4.5l1.5-1M10.5 9.5l1.5 1M11 7h1.5"/></svg>
        <h3>Speaking</h3>
        <p>Veridan is the hub — but it's not the limit.<br>We also offer:</p>
        <svg class="arrow" viewBox="0 0 12 12" fill="none" stroke="#b4bacb" stroke-width="1.2"><path d="M2 6h8M7 3l3 3-3 3"/></svg>
      </div>
      <div class="service alt">
        <svg class="icon" viewBox="0 0 14 14" fill="none" stroke="#1d4ed8" stroke-width="1.4"><circle cx="7" cy="2.5" r="1.2"/><path d="M7 4L3.5 12.5M7 4l3.5 8.5M5 8.5h4"/></svg>
        <h3>Implementation</h3>
        <p>Annual planning sprints, compensation design, org structure redesign, KPI dashboards, automation strategy, and financial modeling — executed alongside your team</p>
        <svg class="arrow" viewBox="0 0 12 12" fill="none" stroke="#b4bacb" stroke-width="1.2"><path d="M2 6h8M7 3l3 3-3 3"/></svg>
      </div>
      <div class="service">
        <svg class="icon" viewBox="0 0 14 14" fill="none" stroke="#1d4ed8" stroke-width="1.4"><circle cx="7" cy="6" r="1.5"/><path d="M4 9a4.2 4.2 0 1 1 6 0M2.3 11a6.5 6.5 0 1 1 9.4 0M7 7.5v5"/></svg>
        <h3>Podcast</h3>
        <p>Annual planning sprints, compensation design, org structure redesign, KPI dashboards, automation strategy, and financial modeling — executed alongside your team</p>
        <svg class="arrow" viewBox="0 0 12 12" fill="none" stroke="#b4bacb" stroke-width="1.2"><path d="M2 6h8M7 3l3 3-3 3"/></svg>
      </div>
      <div class="service alt">
        <svg class="icon" viewBox="0 0 14 14" fill="#1d4ed8"><circle cx="7" cy="5" r="1.8"/><circle cx="3" cy="6" r="1.4"/><circle cx="11" cy="6" r="1.4"/><path d="M4 11a3 3 0 0 1 6 0zM0.5 11a2.5 2.5 0 0 1 4-2l-.5 2zM13.5 11a2.5 2.5 0 0 0-4-2l.5 2z"/></svg>
        <h3>Coaching &amp; Consulting</h3>
        <p>Executive coaching, CFO-level advisory, leadership development arcs, and strategic planning support for owners and senior teams.</p>
        <svg class="arrow" viewBox="0 0 12 12" fill="none" stroke="#b4bacb" stroke-width="1.2"><path d="M2 6h8M7 3l3 3-3 3"/></svg>
      </div>
    </div>
    <p class="close">The platform allows you to start with structured learning. From there, you can deepen the work — through coaching, implementation, or advisory engagement.</p>
  </div>
</section>

<section class="featured">
  <div class="featured-card">
    <div class="badge"><svg width="16" height="16" viewBox="0 0 16 16" fill="none" stroke="#1d4ed8" stroke-width="1.3"><rect x="1.5" y="2.5" width="13" height="11" rx="1.5"/><path d="M4 6h4M4 9h2M9 10l2-3 2 2"/></svg></div>
    <h2>A Featured Path for Surveying Professionals</h2>
    <p>We collaborate with professional associations to deliver business-focused continuing education tailored for surveying companies.</p>
    <p>If you are part of a surveying association, explore our co-branded learning opportunities designed specifically for firm owners, managers, and emerging leaders in your field.</p>
    <a class="btn btn-primary">Launch Internal Audit</a>
  </div>
</section>

<section class="closing">
  <h2>Build a Better Business — <span>Not Just a Better Resume</span></h2>
  <p>Continuing education should not be an obligation you check off.<br>It should be a lever you pull.<br>Veridan exists to help professional firms build margin, clarity, culture, and long-term value —<br>one practical, applied learning experience at a time.</p>
  <div class="closing-ctas"><a class="btn btn-primary">Explore the Platform</a><a class="btn btn-teal">View Learning Paths</a><a class="btn btn-ghost">Book a Conversation</a></div>
</section>

<footer class="site-footer">
  <div class="wrap">
    <div class="footer-cols">
      <div><div class="footer-brand">Veridan</div><p class="about">Leading the integration of financial rigor and leadership identity for professional firms.</p></div>
      <div><h4>Platform</h4><ul><li>Courses</li><li>Assessments</li><li>Analytics</li></ul></div>
      <div><h4>Company</h4><ul><li>About</li><li>Careers</li><li>Contact</li></ul></div>
      <div class="subscribe"><h4>Subscribe</h4><p>Executive insights delivered monthly.</p>
        <div class="sub-form"><div class="sub-input">Email address</div><div class="sub-btn"><svg width="12" height="12" viewBox="0 0 12 12" fill="none" stroke="#fff" stroke-width="1.3"><path d="M1.5 1.5l9 4.5-9 4.5 1.5-4.5z"/></svg></div></div>
      </div>
    </div>
    <div class="footer-bottom"><span>© 2024 Veridan Platform. All rights reserved.</span><nav><span>Privacy Policy</span><span>Terms of Service</span></nav></div>
  </div>
</footer>

</body>
</html>
```